Pet business needs a business card

Pet shop needs a business card. Like dark background and and debased look.

Hedgerowpups
Lindelaan 27
B - 3270 Korbeek
Belgium

www.hedgerowpups.example
mail@hedgerowpups.example
Phone +32471869203

I will ad a tagline shortly.

Industry/Entity Type

Shop

Font styles to use
Sans Serif

Requirements
Must have
• Must be possible to print the card debased. See example image.

```html
<!DOCTYPE html>
<html lang="en">
<head>
<meta charset="utf-8">
<title>Hedgerowpups business card</title>
<link href="https://fonts.googleapis.com/css2?family=Open+Sans:wght@400;600;700&display=swap" rel="stylesheet">
<style>
  :root {
    --page-bg: #b9b9b9;
    --card-bg: #2b3038;
    --card-edge: #23272e;
    --emboss: #20242a;
    --emboss-light: #3a404a;
    --orange: #f3a23a;
    --olive: #8a8770;
    --font-body: "Open Sans", Arial, sans-serif;
  }
  * { box-sizing: border-box; margin: 0; padding: 0; }
  html, body { width: 1200px; height: 900px; overflow: hidden; }
  body {
    background: var(--page-bg);
    font-family: var(--font-body);
    position: relative;
  }
  .card {
    position: absolute;
    width: 560px;
    height: 320px;
    background: var(--card-bg);
    border: 1px solid var(--card-edge);
  }
  .card--back { left: 70px; top: 110px; }
  .card--front { left: 570px; top: 470px; }

  /* Back: blind-embossed name */
  .emboss-name {
    position: absolute;
    left: 0; right: 0; top: 50%;
    transform: translateY(-50%);
    text-align: center;
    font-size: 46px;
    font-weight: 700;
    color: var(--emboss);
    text-shadow: 0 1px 0 var(--emboss-light);
    letter-spacing: 0.5px;
  }

  /* Front */
  .person {
    position: absolute;
    left: 46px; top: 34px;
  }
  .person-name {
    font-size: 19px;
    font-weight: 600;
    letter-spacing: 0.3px;
    line-height: 1.1;
  }
  .person-name .given { color: var(--orange); }
  .person-name .family { color: var(--olive); }
  .person-role {
    font-size: 12px;
    color: var(--orange);
    margin-top: 4px;
  }
  .contact-list {
    position: absolute;
    left: 26px; top: 104px;
    list-style: none;
  }
  .contact-list li {
    display: flex;
    align-items: center;
    gap: 10px;
    font-size: 13px;
    color: var(--orange);
    line-height: 20px;
  }
  .contact-list svg { width: 12px; height: 12px; flex: none; }
  .address {
    position: absolute;
    right: 40px; top: 96px;
    font-style: normal;
    font-size: 13px;
    font-weight: 600;
    color: var(--olive);
    line-height: 20px;
    text-transform: uppercase;
    letter-spacing: 0.3px;
  }
  .brand {
    position: absolute;
    left: 30px; bottom: 36px;
    display: flex;
    align-items: center;
    gap: 12px;
  }
  .brand-dot {
    width: 16px; height: 16px;
    border-radius: 50%;
    background: var(--orange);
  }
  .brand-name {
    font-size: 40px;
    font-weight: 700;
    color: var(--orange);
    line-height: 1;
  }
</style>
</head>
<body>
  <section class="card card--back" aria-label="Card back">
    <div class="emboss-name">Hedgerowpups</div>
  </section>

  <section class="card card--front" aria-label="Card front">
    <div class="person">
      <div class="person-name"><span class="given">PIETER</span> <span class="family">CLAES</span></div>
      <div class="person-role">Director</div>
    </div>

    <ul class="contact-list">
      <li>
        <svg viewBox="0 0 12 12" aria-hidden="true"><rect x="0.5" y="0.5" width="11" height="11" rx="2" fill="none" stroke="var(--olive)"/><rect x="4" y="2.5" width="4" height="7" rx="0.8" fill="var(--olive)"/></svg>
        +3 2471 869 203
      </li>
      <li>
        <svg viewBox="0 0 12 12" aria-hidden="true"><rect x="0.5" y="0.5" width="11" height="11" rx="2" fill="none" stroke="var(--olive)"/><circle cx="6" cy="6" r="3" fill="none" stroke="var(--olive)"/></svg>
        www.hedgerowpups.example
      </li>
      <li>
        <svg viewBox="0 0 12 12" aria-hidden="true"><rect x="0.5" y="0.5" width="11" height="11" rx="2" fill="none" stroke="var(--olive)"/><path d="M2.5 4 L6 7 L9.5 4" fill="none" stroke="var(--olive)"/></svg>
        mail@hedgerowpups.example
      </li>
    </ul>

    <address class="address">
      Lindelaan 27<br>
      B - 3270 Korbeek<br>
      Belgium
    </address>

    <div class="brand">
      <span class="brand-dot" aria-hidden="true"></span>
      <span class="brand-name">Hedgerowpups</span>
    </div>
  </section>
</body>
</html>
```